Dental Specialist Needs a Business Card

We are a state of the art dental specialty office and need a business card that looks modern but professional.
I have provided our logo design in both vertical and horizontal. We use the design on letterhead in the vertical format but provided both forms for you. Thanks

Please add the address, phone and fax numbers I listed to all designs and please leave a space for website and for my employee name on each design. Thanks 2847 Halloway Avenue, Suite K East Marlow, NY 14391 Phone (716)382-9157 Fax:(716)382-9150 My name is Miles R.Dunford,D.D.S. If you want to show it with my name but the design needs to allow for the name to be switched.

Industry/Entity Type

Business

```html
<!DOCTYPE html>
<html lang="en">
<head>
<meta charset="utf-8">
<title>Keystone Endodontics P.C. – Business Card</title>
<link href="https://fonts.googleapis.com/css2?family=Roboto:wght@400;500;700&display=swap" rel="stylesheet">
<style>
  :root {
    --backdrop: #1b1b1b;
    --card: #fbfcfd;
    --ink: #111418;
    --ink-soft: #2a2d31;
    --brand-blue: #3a9ad9;
    --brand-green: #7dbb3a;
    --wash: #e6eef6;
  }
  * { margin: 0; padding: 0; box-sizing: border-box; }
  html, body {
    width: 1200px; height: 1000px; overflow: hidden;
    background: var(--backdrop);
    font-family: "Roboto", Arial, sans-serif;
  }
  .business-card {
    position: absolute; left: 110px; top: 220px;
    width: 980px; height: 560px;
    background: radial-gradient(ellipse at 18% 40%, var(--wash) 0%, var(--card) 55%);
    box-shadow: 0 18px 40px rgba(0,0,0,0.5);
  }
  .brand {
    position: absolute; left: 110px; top: 200px;
    display: flex; align-items: center; gap: 16px;
  }
  .brand-dot {
    width: 44px; height: 44px; border-radius: 50%;
    background: var(--brand-blue);
  }
  .brand-name {
    font-weight: 700; font-size: 30px; line-height: 1.15;
    color: var(--ink);
    letter-spacing: 0.5px;
  }
  .contact {
    position: absolute; left: 560px; top: 190px; width: 360px;
    color: var(--ink);
  }
  .rule { height: 2px; width: 100%; }
  .rule-blue { background: linear-gradient(90deg, rgba(58,154,217,0) 0%, var(--brand-blue) 100%); }
  .rule-green { background: linear-gradient(90deg, rgba(125,187,58,0) 0%, var(--brand-green) 100%); }
  .person-name {
    font-weight: 700; font-size: 26px; padding: 12px 0 12px 40px;
  }
  .person-name .credential { font-weight: 400; }
  .phones { margin: 26px 0 0 0; font-size: 22px; line-height: 1.3; color: var(--ink-soft); }
  .phones b { display: inline-block; width: 26px; color: var(--ink); }
  .address { margin-top: 20px; font-size: 22px; line-height: 1.3; color: var(--ink-soft); }
  .website-space { margin-top: 18px; height: 26px; }
</style>
</head>
<body>
  <section class="business-card">
    <div class="brand">
      <span class="brand-dot"></span>
      <span class="brand-name">Keystone<br>Endodontics P.C.</span>
    </div>
    <div class="contact">
      <div class="rule rule-blue"></div>
      <p class="person-name">Miles R. Dunford <span class="credential">(D.D.S.)</span></p>
      <div class="rule rule-green"></div>
      <p class="phones"><b>P</b>(716) 382-9157<br><b>F</b>(716) 382-9150</p>
      <p class="address">2847 Halloway Avenue,<br>Suite K, East Marlow<br>NY 14391</p>
      <div class="website-space"></div>
    </div>
  </section>
</body>
</html>
```